ORVAN 2 pocket folder
ORVAN Group LLC
ORVAN 2 pocket folder - Construction
Creative Brief
Construction
federal government, corporate
folder must have slot on inside for business card
Ggmmg Ggmmg

```html
<!DOCTYPE html>
<html lang="en">
<head>
<meta charset="utf-8">
<title>ORVAN Group LLC – Two Pocket Folder</title>
<link href="https://fonts.googleapis.com/css2?family=Open+Sans:wght@400;600;700&display=swap" rel="stylesheet">
<style>
:root{
  --purple:#4b3d8f;
  --purple-dark:#3a2e77;
  --green:#7cc242;
  --sky-top:#eef3f9;
  --sky-mid:#d9e4f1;
  --sky-low:#c3d3e6;
  --paper:#ffffff;
  --paper-shade:#e9ebee;
  --ink:#3b3b45;
  --stage:#e6e7e9;
  --photo-a:#8ea3bd;
  --photo-b:#5d6f8c;
  --photo-c:#b9c6d6;
}
*{box-sizing:border-box;margin:0;padding:0}
html,body{width:1200px;height:841px;overflow:hidden}
body{background:var(--stage);font-family:"Open Sans",Arial,sans-serif;color:var(--ink);position:relative}
.spread{position:absolute;left:210px;width:780px;height:396px;display:flex;box-shadow:0 6px 14px rgba(0,0,0,.18)}
.spread--inside{top:18px}
.spread--outside{top:428px}
.panel{position:relative;width:390px;height:396px;overflow:hidden}
.sky{position:absolute;inset:0;background:linear-gradient(160deg,var(--sky-top) 0%,var(--sky-mid) 55%,var(--sky-low) 100%)}
.wordmark{font-weight:700;color:var(--purple);letter-spacing:.5px;display:inline-flex;align-items:center;gap:4px}
.wordmark .mark{display:inline-block;background:var(--purple)}
/* inside left */
.about{position:absolute;left:40px;top:26px;width:310px;text-align:center;font-size:5.6px;line-height:1.45}
.about h2{font-size:8px;font-weight:600;color:var(--purple);letter-spacing:.4px}
.about h3{font-size:7.5px;font-weight:600;color:var(--purple);margin-top:6px}
.about p{text-align:justify;margin-top:3px}
.values{text-align:left;margin-top:3px}
.values li{list-style:none;padding-left:26px;text-indent:-26px;margin-top:2px}
.values b{color:var(--green);font-weight:600}
.pocket{position:absolute;left:0;top:0}
.thumbs{position:absolute;left:20px;top:278px;display:flex;gap:10px;align-items:flex-end}
.thumb{width:34px;height:24px;background:linear-gradient(135deg,var(--photo-c),var(--photo-a))}
.thumb--tall{height:34px;width:26px}
.pocket-logo{position:absolute;left:0;width:300px;top:362px;text-align:center;font-size:10px}
/* card slot */
.card{position:absolute;left:88px;top:282px;width:146px;height:86px;display:flex}
.card__front{width:66px;height:86px;background:var(--paper);border-radius:6px 14px 3px 3px;padding:8px 5px;font-size:3.6px;line-height:1.4}
.card__front .wordmark{font-size:10px;margin-bottom:14px}
.card__back{flex:1;margin-left:4px;border:1px solid #cfcaf0;border-left:none;color:#fff;padding:10px 6px;text-align:right}
.card__name{font-size:8px}
.card__role{font-size:6.5px;font-weight:600}
.card__addr{font-size:3.6px;margin-top:16px;line-height:1.4}
/* outside left */
.back{background:linear-gradient(90deg,var(--paper-shade),var(--paper) 60%)}
.back .wordmark{position:absolute;right:22px;top:20px;font-size:14px}
.back__intro{position:absolute;left:10px;top:42px;width:160px;text-align:center}
.tagline-stack{font-size:7px;color:var(--purple);line-height:1.2;margin-top:40px}
.tagline-stack strong{display:block;color:var(--green);font-weight:600;font-size:7.5px}
.back__intro p{text-align:justify;font-size:4.2px;line-height:1.5;margin-top:6px}
.divider{position:absolute;left:195px;top:42px;width:1px;height:320px;background:#bbb}
.team-photo{position:absolute;left:0;top:212px;width:176px;height:78px;background:linear-gradient(180deg,#c9d6cf,#8d9a95 60%,#3e454d)}
.contact{position:absolute;left:200px;top:322px;width:90px;text-align:center;font-size:3.8px;line-height:1.45}
.contact b{font-weight:700}
/* outside right */
.front .wordmark{position:absolute;left:0;right:0;justify-content:center;top:14px;font-size:17px}
.front__tag{position:absolute;left:0;right:0;top:42px;text-align:center;font-size:7.6px;color:var(--purple);font-variant:small-caps;letter-spacing:.2px}
.diamond{position:absolute;width:56px;height:56px;transform:rotate(45deg);border-radius:4px}
.diamond--green{background:var(--green)}
.diamond--purple{background:var(--purple)}
.diamond--photo{background:linear-gradient(135deg,var(--photo-c),var(--photo-b))}
.diamond--soft{background:linear-gradient(135deg,#dde6f1,#a9bcd3);opacity:.85}
.front__band{position:absolute;left:0;right:0;bottom:0;height:12px;background:var(--green);color:#fff;font-size:6px;font-weight:600;text-align:center;line-height:12px}
.side-photo{position:absolute;left:390px;top:0;width:0}
</style>
</head>
<body>

<!-- Inside of folder -->
<section class="spread spread--inside" aria-label="Folder inside">
  <div class="panel">
    <div class="sky" role="img" aria-label="Faded low-angle photo of glass office towers against sky"></div>
    <div class="about">
      <h2>WHO WE ARE</h2>
      <h2>About ORVAN</h2>
      <p>Established in 2008, ORVAN is a minority-owned small business providing construction services to public and private clients across the region. ORVAN combines proven practices, strategies and project delivery methods in project management, engineering and construction, using disciplined execution shaped to each client's mission, objectives and goals with the highest level of quality in mind.</p>
      <h3>Mission:</h3>
      <p>We exist to create value for our clients by delivering high-quality and cost effective solutions for each engagement.</p>
      <h3>Vision:</h3>
      <p>To be recognized as an industry leader in providing valuable professional, technical and construction solutions for our clients.</p>
      <h3>Core Values:</h3>
      <ul class="values">
        <li><b>Integrity</b> – We will carry out all business with the highest standards of transparency and ethical responsibility to earn the trust of our clients and partners.</li>
        <li><b>Work</b> – We will provide exceptional performance, build lasting win-win relationships and focus on being a value-added partner.</li>
        <li><b>Excellence</b> – We will attract and retain people who think boldly and bring a "can-do" attitude to their work for our clients.</li>
      </ul>
    </div>
    <svg class="pocket" width="390" height="396" viewBox="0 0 390 396" aria-hidden="true">
      <defs>
        <linearGradient id="pocketWhite" x1="0" y1="0" x2="1" y2="0">
          <stop offset="0" stop-color="#e4e6ea"/><stop offset=".5" stop-color="#ffffff"/><stop offset="1" stop-color="#eef0f3"/>
        </linearGradient>
      </defs>
      <path d="M0 238 Q0 230 10 230 L230 212 Q262 210 280 236 L305 300 L305 396 L0 396 Z" fill="url(#pocketWhite)"/>
    </svg>
    <div class="thumbs">
      <div class="thumb" role="img" aria-label="Small photo of engineers reviewing plans"></div>
      <div class="thumb thumb--tall" role="img" aria-label="Small photo of a high-rise building"></div>
      <div class="thumb" role="img" aria-label="Small photo of a hand drawing plans"></div>
      <div class="thumb" role="img" aria-label="Small photo of a team meeting"></div>
      <div class="thumb" role="img" aria-label="Small photo of blueprints"></div>
    </div>
    <div class="pocket-logo"><span class="wordmark">ORVAN</span></div>
  </div>

  <div class="panel">
    <div class="sky" role="img" aria-label="Faded photo of glass office towers"></div>
    <svg class="pocket" width="390" height="396" viewBox="0 0 390 396" aria-hidden="true">
      <defs>
        <linearGradient id="pocketPurple" x1="0" y1="0" x2="1" y2="0">
          <stop offset="0" stop-color="#3d3080"/><stop offset=".5" stop-color="#4b3d8f"/><stop offset="1" stop-color="#433687"/>
        </linearGradient>
      </defs>
      <path d="M0 396 L0 330 Q8 270 20 246 Q34 218 70 214 L390 212 L390 396 Z" fill="url(#pocketPurple)"/>
    </svg>
    <div class="card">
      <div class="card__front">
        <div class="wordmark"><span class="mark" style="width:5px;height:5px"></span>ORVAN</div>
        <b>Contact Information:</b><br>ORVAN Group LLC<br>410 Harbor Point Dr, Ste 200<br>Lakeview, ST 00000<br>P: 555-010-2481<br>F: 555-010-2482
      </div>
      <div class="card__back">
        <div class="card__name">Daniel Reyes</div>
        <div class="card__role">Director</div>
        <div class="card__addr"><b>Branch Office:</b><br>22 Mill Creek Road<br>Riverton, ST 00000<br>P: 555-010-7730<br>Email: info@orvangroupllc.com</div>
      </div>
    </div>
  </div>
</section>

<!-- Outside of folder -->
<section class="spread spread--outside" aria-label="Folder outside">
  <div class="panel back">
    <div class="wordmark"><span class="mark" style="width:6px;height:6px"></span>ORVAN</div>
    <div class="back__intro">
      <div class="tagline-stack">YOUR PARTNERS<br>IN<strong>PROJECT DELIVERY</strong></div>
      <p>ORVAN Group LLC is a minority-owned professional construction services firm working in project and construction management, general contracting, design-build and engineering, with the capacity to support the full project life cycle from inception through start-up and operation. We serve clients in the public, municipal, commercial and residential markets, delivering strong client service, quality results and lasting value across every project phase.</p>
    </div>
    <div class="team-photo" role="img" aria-label="Photo of business team standing at a large office window at sunrise"></div>
    <div class="divider"></div>
    <div class="contact">
      <b>Contact Information:</b><br>ORVAN Group LLC<br>410 Harbor Point Dr, Ste 200<br>Lakeview, ST 00000<br>P: 555-010-2481<br>F: 555-010-2482<br><br>
      <b>Branch Office:</b><br>22 Mill Creek Road<br>Riverton, ST 00000<br>P: 555-010-7730<br>Email: info@orvangroupllc.com
    </div>
  </div>

  <div class="panel front">
    <div class="sky" role="img" aria-label="Faded architectural photo of modern towers"></div>
    <div class="wordmark"><span class="mark" style="width:8px;height:8px"></span>ORVAN</div>
    <div class="front__tag">Your Partner in Project Delivery</div>
    <div class="diamond diamond--soft" style="left:-18px;top:250px" role="img" aria-label="Faded photo of a glass building"></div>
    <div class="diamond diamond--green" style="left:10px;top:180px"></div>
    <div class="diamond diamond--photo" style="left:82px;top:158px" role="img" aria-label="Photo of engineers in hard hats"></div>
    <div class="diamond diamond--purple" style="left:172px;top:134px"></div>
    <div class="diamond diamond--photo" style="left:246px;top:184px" role="img" aria-label="Photo of colleagues at a desk"></div>
    <div class="diamond diamond--photo" style="left:46px;top:240px;width:50px;height:50px" role="img" aria-label="Photo of a glass office tower"></div>
    <div class="diamond diamond--photo" style="left:122px;top:216px;width:78px;height:78px" role="img" aria-label="Portrait photo of a senior executive"></div>
    <div class="diamond diamond--photo" style="left:220px;top:258px" role="img" aria-label="Photo of a business team"></div>
    <div class="diamond diamond--soft" style="left:112px;top:310px;width:64px;height:64px" role="img" aria-label="Faded technical drawing of a building"></div>
    <div class="diamond diamond--photo" style="left:190px;top:320px;width:46px;height:46px" role="img" aria-label="Photo of smiling professionals"></div>
    <div class="front__band">www.orvangroupllc.com</div>
  </div>
</section>

</body>
</html>
```